Gilded Realty website

full website from start to finish. I would like something like this -
https://www.brindlecovemanors.com/
http://plumhavenlots.com/

Target Market(s)

real estate investors

Industry/Entity Type

Real Estate

Number of Pages Required

5+ page

Font styles to use
Sans Serif

Colors

Designer to choose colors to be used in the design.

Requirements
Must have
• translated in English, Spanish and japanese

```html
<!DOCTYPE html>
<html lang="en">
<head>
<meta charset="utf-8">
<title>Gilded Realty</title>
<link href="https://fonts.googleapis.com/css2?family=Montserrat:wght@400;500;600;700&family=Lora:ital@1&display=swap" rel="stylesheet">
<style>
:root{
  --orange:#f7941d;
  --white:#ffffff;
  --ink:#333333;
  --muted:#666666;
  --line:#e4e4e4;
  --contact-bg:#4b4b4b;
  --footer-bg:#262626;
  --hero-top:#161a3a;
  --hero-bottom:#2a2c3e;
}
*{margin:0;padding:0;box-sizing:border-box}
html,body{width:1200px;height:3010px;overflow:hidden}
body{font-family:"Montserrat",sans-serif;color:var(--ink);background:var(--white);position:relative}
section,header,footer,nav{position:absolute;left:0;width:1200px}
.abs{position:absolute}

/* header + hero */
.hero{top:0;height:596px}
.hero-photo{position:absolute;inset:0;background:linear-gradient(180deg,#0f1330 0%,#1e2350 35%,#3a3140 62%,#1c2030 100%)}
.site-nav{top:0;height:88px;display:flex;align-items:center;padding:0 112px;color:var(--white);font-size:14px}
.brand{font-size:22px;font-weight:500;margin-right:28px}
.nav-links{display:flex;gap:26px;font-size:13px}
.nav-call{margin-left:30px;display:flex;align-items:center;gap:8px;font-size:13px}
.nav-call b{font-weight:700}
.nav-social{display:flex;gap:22px;margin-left:22px;font-size:12px;font-weight:600}
.nav-lang{margin-left:auto;display:flex;align-items:center;gap:6px}
.nav-lang span{width:22px;height:22px;border-radius:50%;background:#c8cde0;display:block}
.hero-title{top:312px;width:1200px;text-align:center;color:var(--white);font-size:38px;font-weight:700}
.hero-title em{font-style:normal;color:var(--orange)}
.btn{display:inline-block;background:var(--orange);color:var(--white);font-weight:700;font-size:12px;letter-spacing:.5px;text-transform:uppercase}
.hero-btn{top:378px;left:532px;width:132px;height:42px;line-height:42px;text-align:center}
.hero-pager{top:538px;width:1200px;text-align:center;color:var(--orange);font-size:10px;letter-spacing:.5px}

/* welcome */
.welcome{top:596px;height:420px}
.welcome-bar{left:766px;top:0;width:224px;height:420px;background:var(--orange)}
.welcome-text{left:112px;top:78px;width:450px}
.welcome-text h2{color:var(--orange);font-size:25px;font-weight:700;line-height:28px;text-transform:uppercase}
.lead{font-size:16px;color:var(--muted);line-height:22px;margin-top:16px}
.body-copy{font-size:12px;color:var(--ink);line-height:20px;margin-top:18px}
.text-link{display:inline-block;margin-top:20px;color:var(--orange);font-size:12px;font-weight:700;text-transform:uppercase;border-bottom:2px solid var(--orange);padding-bottom:2px}
.video{left:670px;top:80px;width:414px;height:270px;background:linear-gradient(160deg,#6c6f8a,#34364c);box-shadow:0 4px 14px rgba(0,0,0,.3)}
.play{position:absolute;left:184px;top:112px;width:48px;height:48px;border-radius:50%;background:#000}

/* featured */
.featured{top:1016px;height:510px}
.featured-photo{position:absolute;inset:0;background:linear-gradient(90deg,#6d6a66 0%,#a39c95 25%,#2e2e30 45%,#3a3938 65%,#cfcac4 100%)}
.featured-shade{position:absolute;inset:0;background:linear-gradient(0deg,rgba(0,0,0,.35),rgba(0,0,0,0) 60%)}
.arrow-box{width:36px;height:36px;border:2px solid var(--white);display:flex;align-items:center;justify-content:center}
.featured-kicker{left:170px;top:334px;color:var(--white);font-size:22px;letter-spacing:.5px}
.featured-title{left:168px;top:362px;color:var(--white);font-family:"Lora",serif;font-style:italic;font-size:46px}
.featured-price{left:170px;top:428px;color:var(--white);font-family:"Lora",serif;font-style:italic;font-size:20px}
.featured-btn{left:890px;top:374px;width:134px;height:42px;border:2px solid var(--white);color:var(--white);font-size:12px;font-weight:700;text-align:center;line-height:38px;text-transform:uppercase}

/* listings */
.listings{top:1526px;height:542px}
.section-title{width:1200px;text-align:center;font-size:22px;color:var(--ink);letter-spacing:.5px;top:40px}
.card{top:88px;width:306px;height:386px;background:var(--white);box-shadow:0 2px 8px rgba(0,0,0,.18)}
.card-img{height:220px}
.card-addr{text-align:center;padding-top:14px;font-size:15px;line-height:22px}
.card-addr span{color:var(--muted)}
.card-price{margin-top:12px;height:42px;background:#f3f3f3;text-align:center;line-height:42px;font-weight:700;font-size:15px}
.card-meta{display:flex;justify-content:space-around;height:52px;align-items:center;font-size:13px;color:var(--muted)}
.card-meta i{font-style:normal;display:inline-block;width:14px;height:12px;border:1.5px solid #999;margin-right:6px;vertical-align:-1px}

/* testimonials */
.testimonials{top:2068px;height:382px}
.testi-photo{position:absolute;inset:0;background:linear-gradient(90deg,#e6e6e2,#f4f4f1 55%,#c9ccc4)}
.testi-text{left:112px;top:84px;width:490px;color:var(--white)}
.testi-text h3{font-size:22px;font-weight:400}
.testi-text p{font-size:12px;line-height:22px;margin-top:20px}
.person{display:flex;align-items:center;gap:14px;margin-top:28px}
.avatar{width:74px;height:74px;border-radius:50%;border:4px solid var(--white);background:#d9b8a3}
.person b{display:block;font-size:15px;font-weight:500}
.person small{font-size:11px}

/* contact */
.contact{top:2450px;height:370px;background:var(--contact-bg)}
.map{position:absolute;inset:0;background:radial-gradient(circle at 70% 40%,#575757,#4b4b4b 60%)}
.info-box{left:104px;top:56px;width:266px;height:286px;background:rgba(60,60,60,.8)}
.info-row{display:flex;align-items:center;gap:20px;padding:0 16px;height:95px;border-bottom:1px solid #5a5a5a;color:var(--white);font-size:12px;line-height:20px}
.info-row:last-child{border-bottom:0}
.icon-dot{width:46px;height:46px;border-radius:50%;background:var(--orange);flex:none;display:flex;align-items:center;justify-content:center}
.contact-form{left:512px;top:52px;width:572px;color:var(--white)}
.contact-form h3{font-size:22px;font-weight:400;margin-bottom:20px}
.field{border:1px solid #6a6a6a;background:#464646;height:34px;font-size:11px;padding:8px 6px;color:#ddd}
.row2{display:flex;gap:8px;margin-bottom:16px}
.row2 .field{flex:1}
.submit{width:146px;height:38px;line-height:38px;text-align:center;margin-top:16px;font-size:14px;font-weight:600;text-transform:none}

.footer-nav{top:2820px;height:54px;background:var(--orange);display:flex;justify-content:center;align-items:center;gap:30px;color:var(--white);font-size:13px}
.site-footer{top:2874px;height:136px;background:var(--footer-bg);color:var(--white);text-align:center}
.footer-social{display:flex;justify-content:center;gap:30px;margin-top:42px;font-size:12px;font-weight:600}
.copyright{margin-top:28px;font-size:11px;color:#ddd}
</style>
</head>
<body>

<section class="hero">
  <div class="hero-photo" role="img" aria-label="Evening photo of a luxury residential tower beside a canal lined with palm trees"></div>
  <nav class="site-nav">
    <div class="brand">Gilded Realty</div>
    <div class="nav-links"><span>Home</span><span>Properties</span><span>Our Business</span><span>Contact Us</span></div>
    <div class="nav-call">
      <svg width="14" height="14" viewBox="0 0 24 24"><path fill="#fff" d="M6.6 10.8a15 15 0 0 0 6.6 6.6l2.2-2.2c.3-.3.7-.4 1-.2 1.1.4 2.3.6 3.6.6.6 0 1 .4 1 1V20c0 .6-.4 1-1 1A17 17 0 0 1 3 4c0-.6.4-1 1-1h3.5c.6 0 1 .4 1 1 0 1.3.2 2.5.6 3.6.1.3 0 .7-.2 1z"/></svg>
      <span><b>Call Us :</b> 1-800 555 0142</span>
    </div>
    <div class="nav-social"><span>Feed</span><span>Page</span><span>Work</span></div>
    <div class="nav-lang"><span></span>
      <svg width="8" height="6" viewBox="0 0 8 6"><path d="M0 0h8L4 6z" fill="#fff"/></svg></div>
  </nav>
  <h1 class="abs hero-title"><em>Gilded</em> Realty</h1>
  <span class="abs btn hero-btn">Learn More</span>
  <div class="abs hero-pager">⟵ PREVIOUS &nbsp;/&nbsp; NEXT ⟶</div>
</section>

<section class="welcome">
  <div class="abs welcome-bar"></div>
  <div class="abs welcome-text">
    <h2>Welcome to<br>Gilded Realty</h2>
    <p class="lead">Lacus animi eros in wisi urna. Gravida mi eius et eget pede sed ut hendrerit felis etiam at.</p>
    <p class="body-copy">Turpis sit sed in risus pellentesque lacus sed saepe mus sed urna. Dictum neque luctus. Sapien hymenaeos ante lacus in vel ligula eu lacus. Malesuada tortor a. Enim eget pretium vitae ac ut. Eu netus ac nullam lacinia maecenas. Risus sit adipiscing integer rhoncus sem. Sit scelerisque sociis nibh vivamus fermentum.</p>
    <span class="text-link">Take a Tour</span>
  </div>
  <div class="abs video" role="img" aria-label="Video still of rows of small model houses with one red-roofed house lit up">
    <div class="play"><svg width="48" height="48" viewBox="0 0 48 48"><path d="M19 15l15 9-15 9z" fill="#fff"/></svg></div>
  </div>
</section>

<section class="featured">
  <div class="featured-photo" role="img" aria-label="Modern living room with sofa, arc floor lamp, tall windows and floating staircase"></div>
  <div class="featured-shade"></div>
  <div class="abs arrow-box" style="left:112px;top:216px"><svg width="12" height="14" viewBox="0 0 12 14"><path d="M9 1L3 7l6 6" stroke="#fff" stroke-width="2.5" fill="none"/></svg></div>
  <div class="abs arrow-box" style="left:1048px;top:216px"><svg width="12" height="14" viewBox="0 0 12 14"><path d="M3 1l6 6-6 6" stroke="#fff" stroke-width="2.5" fill="none"/></svg></div>
  <div class="abs featured-kicker">FEATURED LISTINGS</div>
  <div class="abs featured-title">Comfort &amp; Style</div>
  <div class="abs featured-price">Price upon Request <span style="color:var(--orange);font-style:normal">⟶</span></div>
  <div class="abs featured-btn">Learn More</div>
</section>

<section class="listings">
  <h2 class="abs section-title" style="font-weight:400">PROPERTY LISTINGS</h2>
  <article class="abs card" style="left:112px">
    <div class="card-img" role="img" aria-label="City street lined with glass office towers" style="background:linear-gradient(180deg,#8fb3d6,#6c7f93)"></div>
    <div class="card-addr">418 Amberline Court<br><span>Halden, NV 89990</span></div>
    <div class="card-price">$8,395,000</div>
    <div class="card-meta"><span><i></i>14,485</span><span><i></i>0</span><span><i></i>0</span></div>
  </article>
  <article class="abs card" style="left:446px">
    <div class="card-img" role="img" aria-label="White modern villa with landscaped garden" style="background:linear-gradient(180deg,#5f8fc9,#c9c3b8 60%,#6f7f4c)"></div>
    <div class="card-addr">418 Amberline Court<br><span>Halden, NV 89990</span></div>
    <div class="card-price">$8,395,000</div>
    <div class="card-meta"><span><i></i>14,485</span><span><i></i>0</span><span><i></i>0</span></div>
  </article>
  <article class="abs card" style="left:778px">
    <div class="card-img" role="img" aria-label="Mansion at dusk with illuminated swimming pool" style="background:linear-gradient(180deg,#2d4a7c,#8c6a3c 55%,#3f8fa0)"></div>
    <div class="card-addr">418 Amberline Court<br><span>Halden, NV 89990</span></div>
    <div class="card-price">$8,395,000</div>
    <div class="card-meta"><span><i></i>14,485</span><span><i></i>0</span><span><i></i>0</span></div>
  </article>
  <svg class="abs" style="left:112px;top:188px" width="36" height="40" viewBox="0 0 36 40"><rect x="1" y="1" width="34" height="38" fill="none" stroke="#fff" stroke-width="2"/><path d="M21 12l-7 8 7 8" stroke="#fff" stroke-width="2.5" fill="none"/></svg>
  <svg class="abs" style="left:1048px;top:188px" width="36" height="40" viewBox="0 0 36 40"><rect x="1" y="1" width="34" height="38" fill="none" stroke="#fff" stroke-width="2"/><path d="M15 12l7 8-7 8" stroke="#fff" stroke-width="2.5" fill="none"/></svg>
</section>

<section class="testimonials">
  <div class="testi-photo" role="img" aria-label="Bright white living room with armchair, floor lamp and framed pictures"></div>
  <svg class="abs" style="left:0;top:0" width="642" height="382" viewBox="0 0 642 382"><polygon points="0,0 588,0 642,382 0,382" fill="#f7941d"/></svg>
  <div class="abs testi-text">
    <h3>TESTIMONIALS</h3>
    <p>"Velit condimentum molestie eu eleifend leo. Egestas vitae ac velit et ut. Et elementum dolor quisque nec dolor posuere rhoncus wisi. Ultricies donec sollicitudin. Elit hac vestibulum. Nam vel volutpat. "</p>
    <div class="person">
      <div class="avatar" role="img" aria-label="Client portrait"></div>
      <div><b>Mira</b><small>Lorium ipsum</small></div>
    </div>
  </div>
</section>

<section class="contact">
  <div class="map" role="img" aria-label="Faded regional street map"></div>
  <div class="abs info-box">
    <div class="info-row"><div class="icon-dot"><svg width="18" height="22" viewBox="0 0 18 22"><path d="M9 0a8 8 0 0 0-8 8c0 6 8 14 8 14s8-8 8-14a8 8 0 0 0-8-8zm0 11a3 3 0 1 1 0-6 3 3 0 0 1 0 6z" fill="#fff"/></svg></div><span>Gilded Realty<br>#123 Lorium ipsum,<br>Streer name, Pincode City.</span></div>
    <div class="info-row"><div class="icon-dot"><svg width="20" height="20" viewBox="0 0 24 24"><path fill="#fff" d="M6.6 10.8a15 15 0 0 0 6.6 6.6l2.2-2.2c.3-.3.7-.4 1-.2 1.1.4 2.3.6 3.6.6.6 0 1 .4 1 1V20c0 .6-.4 1-1 1A17 17 0 0 1 3 4c0-.6.4-1 1-1h3.5c.6 0 1 .4 1 1 0 1.3.2 2.5.6 3.6.1.3 0 .7-.2 1z"/></svg></div><span>1-800 555 0198</span></div>
    <div class="info-row"><div class="icon-dot"><svg width="22" height="16" viewBox="0 0 22 16"><rect width="22" height="16" rx="1" fill="#fff"/><path d="M1 1l10 8 10-8" stroke="#f7941d" stroke-width="2" fill="none"/></svg></div><span>hello@gildedrealty.com</span></div>
  </div>
  <div class="abs contact-form">
    <h3 style="text-align:center;padding-right:140px">CONTACT US</h3>
    <div class="row2"><div class="field">Name</div><div class="field">Email</div></div>
    <div class="field" style="margin-bottom:16px">Subject</div>
    <div class="field" style="height:64px">Message</div>
    <div class="btn submit">Submit</div>
  </div>
</section>

<nav class="footer-nav"><span>Home</span><span>Properties</span><span>Our Business</span><span>Contact Us</span></nav>

<footer class="site-footer">
  <div class="footer-social"><span>Folio</span><span>Shots</span><span>Feed</span><span>Page</span><span>Work</span></div>
  <p class="copyright">copyright © 2018 &nbsp; www.gildedrealty.com</p>
</footer>

</body>
</html>
```